DORIVAN
POWER THE FUTURE
Professional
Tobin Rasquelle
2417 Fennimore Lane
Glen Burnie, MD 21060
tobin@dorivan7.com
www.dorivan7.com
I can provide logo as need it.
Logo and write this underneath the logo or where you think it will look better.
Have fun!!

```html
<!DOCTYPE html>
<html lang="en">
<head>
<meta charset="utf-8">
<title>DORIVAN Stationery Concepts</title>
<link rel="stylesheet" href="https://fonts.googleapis.com/css2?family=Michroma&family=Open+Sans:wght@400;600;700&display=swap">
<style>
:root{
  --blue:#1b6fbd;
  --blue-dark:#145a9c;
  --green:#3aa935;
  --yellow:#f3e500;
  --paper:#ffffff;
  --ink:#4a4a4a;
  --grey-text:#6d6d6d;
  --bg-light:#d6d6d6;
  --bg-dark:#9c9c9c;
}
*{box-sizing:border-box;margin:0;padding:0}
html,body{width:1200px;height:377px;overflow:hidden}
body{
  position:relative;
  background:radial-gradient(ellipse at 45% 45%,var(--bg-light) 0%,#bdbdbd 55%,var(--bg-dark) 100%);
  font-family:"Open Sans",Arial,sans-serif;
  color:var(--ink);
}
.brand-title{position:absolute;left:19px;top:158px}
.brand-title .wordmark{
  font-family:"Michroma",Arial,sans-serif;font-size:36px;color:#fff;letter-spacing:1px;line-height:1;
}
.brand-title .tagline{font-size:12px;color:#fff;margin-top:10px;margin-left:52px}

.card{position:absolute;width:130px;height:50px;box-shadow:0 2px 4px rgba(0,0,0,.35);overflow:hidden}
.card-front{background:var(--yellow)}
.card-front .logo{position:absolute;left:8px;top:9px;font-family:"Michroma",Arial,sans-serif;font-size:13px;color:var(--blue)}
.card-front .slogan{position:absolute;left:0;right:0;bottom:0;height:13px;background:var(--blue);color:#fff;font-size:6px;line-height:13px;padding-left:34px;letter-spacing:.5px}
.card-back{background:var(--paper)}
.card-back svg{position:absolute;left:0;top:0}
.card-back .name{position:absolute;left:70px;top:2px;font-size:5px;color:#fff;font-weight:600}
.card-back .logo{position:absolute;left:6px;top:20px;font-family:"Michroma",Arial,sans-serif;font-size:9px;color:var(--blue)}
.card-back .details{position:absolute;left:72px;top:17px;font-size:3.6px;line-height:5px;color:var(--grey-text)}
.card-caption{position:absolute;font-size:5px;color:#fff}

.letterhead{position:absolute;top:22px;width:152px;height:345px;background:var(--paper);box-shadow:0 2px 6px rgba(0,0,0,.35);overflow:hidden}
.letterhead svg{position:absolute;left:0}
.letterhead .head{top:0}
.letterhead .foot{bottom:0}
.letterhead .logo{position:absolute;left:10px;top:24px;font-family:"Michroma",Arial,sans-serif;font-size:12px;color:var(--blue)}
.letterhead .header-info{position:absolute;right:8px;top:6px;font-size:3.6px;line-height:5px;color:#fff;text-align:right}
.letterhead .footer-info{position:absolute;left:0;right:0;bottom:5px;font-size:3.6px;color:#fff;text-align:center}

.envelope{position:absolute;left:895px;width:295px;height:80px;background:var(--paper);box-shadow:0 2px 6px rgba(0,0,0,.35);overflow:hidden}
.envelope svg{position:absolute;left:0;top:0}
.envelope .logo{position:absolute;left:12px;top:32px;font-family:"Michroma",Arial,sans-serif;font-size:13px;color:var(--blue)}
.envelope .return{position:absolute;left:12px;top:50px;font-size:4px;line-height:5.5px;color:var(--grey-text)}
</style>
</head>
<body>

<div class="brand-title">
  <div class="wordmark">DORIVAN</div>
  <div class="tagline">Reliability Concepts</div>
</div>

<!-- business cards -->
<div class="card card-front" style="left:19px;top:238px">
  <div class="logo">DORIVAN</div>
  <div class="slogan">POWER THE FUTURE</div>
</div>
<div class="card card-back" style="left:158px;top:238px">
  <svg width="130" height="50" viewBox="0 0 130 50">
    <path d="M60 0H130V10H60Z" fill="var(--blue)"/>
    <path d="M0 44Q60 30 130 40V50H0Z" fill="var(--green)"/>
  </svg>
  <div class="name">Tobin Rasquelle</div>
  <div class="logo">DORIVAN</div>
  <div class="details">Professional<br>410-555-0182<br>tobin@dorivan7.com<br>www.dorivan7.com</div>
</div>
<div class="card card-front" style="left:19px;top:305px">
  <div class="logo">DORIVAN</div>
  <div class="slogan">POWER THE FUTURE</div>
</div>
<div class="card card-back" style="left:158px;top:305px">
  <svg width="130" height="50" viewBox="0 0 130 50">
    <path d="M60 0H130V10H60Z" fill="var(--blue)"/>
    <path d="M0 44Q60 30 130 40V50H0Z" fill="var(--green)"/>
  </svg>
  <div class="name">Tobin Rasquelle</div>
  <div class="logo">DORIVAN</div>
  <div class="details">Professional<br>410-555-0182<br>tobin@dorivan7.com<br>www.dorivan7.com</div>
</div>
<div class="card-caption" style="left:50px;top:292px">Card front design</div>
<div class="card-caption" style="left:190px;top:292px">Card back design</div>
<div class="card-caption" style="left:50px;top:359px">Card front design</div>
<div class="card-caption" style="left:190px;top:359px">Card back design</div>

<!-- letterheads -->
<div class="letterhead" style="left:329px">
  <svg class="head" width="152" height="60" viewBox="0 0 152 60">
    <path d="M0 0H152V46Q80 14 0 20Z" fill="var(--blue)"/>
    <path d="M0 20Q80 14 152 46" fill="none" stroke="var(--green)" stroke-width="3"/>
  </svg>
  <div class="header-info">2417 Fennimore Lane<br>Glen Burnie, MD 21060<br>tobin@dorivan7.com</div>
  <div class="logo">DORIVAN</div>
  <svg class="foot" width="152" height="30" viewBox="0 0 152 30">
    <path d="M0 10Q80 20 152 8V30H0Z" fill="var(--green)"/>
  </svg>
  <div class="footer-info">www.dorivan7.com</div>
</div>
<div class="letterhead" style="left:511px">
  <svg class="head" width="152" height="60" viewBox="0 0 152 60">
    <path d="M0 0H152V46Q80 14 0 20Z" fill="var(--blue)"/>
    <path d="M0 20Q80 14 152 46" fill="none" stroke="var(--green)" stroke-width="3"/>
  </svg>
  <div class="header-info">2417 Fennimore Lane<br>Glen Burnie, MD 21060<br>tobin@dorivan7.com</div>
  <div class="logo">DORIVAN</div>
  <svg class="foot" width="152" height="30" viewBox="0 0 152 30">
    <path d="M0 8Q80 22 152 10V30H0Z" fill="var(--blue)"/>
  </svg>
  <div class="footer-info">www.dorivan7.com</div>
</div>

<!-- envelopes -->
<div class="envelope" style="top:29px">
  <svg width="295" height="80" viewBox="0 0 295 80">
    <path d="M0 0H295V30Q150 10 0 30Z" fill="var(--green)"/>
    <path d="M0 30Q150 10 295 30" fill="none" stroke="var(--blue)" stroke-width="2"/>
  </svg>
  <div class="logo">DORIVAN</div>
  <div class="return">2417 Fennimore Lane<br>Glen Burnie, MD 21060</div>
</div>
<div class="envelope" style="top:135px">
  <svg width="295" height="80" viewBox="0 0 295 80">
    <path d="M0 0L147 42L295 0" fill="none" stroke="#dcdcdc" stroke-width="1.5"/>
    <path d="M0 80L120 38M295 80L175 38" fill="none" stroke="#e4e4e4" stroke-width="1"/>
  </svg>
</div>
<div class="envelope" style="top:222px;height:70px">
  <svg width="295" height="70" viewBox="0 0 295 70">
    <path d="M0 0L147 38L295 0" fill="none" stroke="#dcdcdc" stroke-width="1.5"/>
  </svg>
</div>
<div class="envelope" style="top:283px;height:76px">
  <svg width="295" height="76" viewBox="0 0 295 76">
    <path d="M0 0H295V28Q150 8 0 28Z" fill="var(--blue)"/>
    <path d="M0 28Q150 8 295 28" fill="none" stroke="var(--green)" stroke-width="2"/>
  </svg>
  <div class="logo">DORIVAN</div>
  <div class="return">2417 Fennimore Lane<br>Glen Burnie, MD 21060</div>
</div>

</body>
</html>
```